New florist business website design

Number 1 want is an easy to navigate & check out website
Needs to be beautiful and eye catching as well.
This is an online only business (no shop front)
Rustic and blush pinks, neutrals, woods, leaves
Customers need to be able to go onto my website, select something they want to buy but have the option to use a drop down box to change colours of the flowers, or add notes to make changes to the arrangement

Industry/Entity Type

Florist

Coding

Coded - Design and coding required

Number of Pages Required

5+ page

Colors
f9d9e8
fff2ec
fffefc

Requirements
Must have
• Drop down menu to take you to other pages for Arrangements, bouquets, everlasting arrangements, gifts, contact
Be able to purchase and “add to basket”
Checkout page
Nice to have
• Be able to add my own photos once I’ve taken new ones
Should not have
• Tacky images or clip art

```html
<!DOCTYPE html>
<html lang="en">
<head>
<meta charset="utf-8">
<title>Fern &amp; Folly — Florist</title>
<link rel="stylesheet" href="https://fonts.googleapis.com/css2?family=Poppins:wght@300;400;500;600;700;800&family=Great+Vibes&display=swap">
<style>
:root{
  --ink:#1c1c1c;
  --text:#444;
  --muted:#777;
  --accent:#e44a68;
  --hero:#f9e3e5;
  --blush:#f9d9e8;
  --cream:#fff2ec;
  --paper:#fffefc;
  --line:#dcdcdc;
  --gold:#f0a53a;
}
*{margin:0;padding:0;box-sizing:border-box}
html,body{width:1200px;height:3955px;overflow:hidden}
body{background:var(--paper);font-family:'Poppins',sans-serif;color:var(--ink);position:relative}
.abs{position:absolute}
.script{font-family:'Great Vibes',cursive;color:var(--accent);font-size:38px;line-height:1}
.heading{font-weight:700;letter-spacing:1px;line-height:1.1;text-transform:uppercase}
.center{left:0;width:1200px;text-align:center}
.btn{background:var(--accent);color:#fff;font-size:13px;font-weight:600;border-radius:20px;display:flex;align-items:center;justify-content:center;letter-spacing:.5px;text-transform:uppercase}
.photo{position:absolute}

/* header */
.hero{left:0;top:0;width:1200px;height:657px;background:linear-gradient(90deg,var(--hero) 0%,#f7e5e3 55%,#efe2dc 100%)}
.brand{left:84px;top:55px;display:flex;align-items:center;gap:10px;font-size:30px;font-weight:400;color:var(--ink)}
.brand .dot{width:12px;height:12px;border-radius:50%;background:var(--accent)}
.nav{left:295px;top:47px;display:flex;gap:28px;font-size:13px;font-weight:500;text-transform:uppercase}
.tools{left:902px;top:44px;display:flex;gap:16px;align-items:center}
.cart{left:1046px;top:43px;font-size:10px;color:var(--muted);line-height:1.3;text-transform:uppercase}
.cart b{color:var(--accent);font-weight:400;display:block}
.badge{left:1021px;top:40px;width:15px;height:15px;border-radius:50%;background:var(--accent);color:#fff;font-size:9px;display:flex;align-items:center;justify-content:center}
.dots{display:flex;gap:6px}
.dots i{width:9px;height:9px;border-radius:50%;background:#ddd;display:block}
.dots i.on{background:var(--accent)}

/* categories */
.cat{top:730px;width:267px;height:252px}
.cat .frame{position:absolute;inset:12px;border:2px solid rgba(255,255,255,.7)}
.cat p{position:absolute;left:30px;top:170px;font-size:12px;color:var(--ink);line-height:1}
.cat p b{display:block;font-size:20px;font-weight:500;margin-top:4px}

/* products */
.prod{top:1798px;width:246px;height:250px;background:var(--cream)}
.prod .img{position:absolute;left:40px;top:-110px;width:166px;height:190px;border-radius:50% 50% 40% 40%}
.prod .info{position:absolute;left:25px;top:107px}
.stars{color:var(--gold);font-size:13px;letter-spacing:2px}
.prod h4{font-size:17px;font-weight:600;margin-top:3px}
.prod .price{font-size:17px;margin-top:1px}
.sw{display:flex;gap:8px;margin-top:12px}
.sw i{display:block;width:32px;height:32px;border:2px solid #f0dcdc;background:#fff;padding:6px}
.sw i span{display:block;width:100%;height:100%;border-radius:50%}

/* steps */
.steps{left:89px;top:2328px;width:565px;height:410px;background:var(--blush)}
.step{left:135px;display:flex;gap:16px}
.step .icon{width:71px;height:71px;background:#fff;display:flex;align-items:center;justify-content:center}
.step h5{font-size:18px;font-weight:600;text-transform:uppercase;margin-top:8px}
.step p{font-size:14px;color:#666;line-height:1.55;margin-top:4px}

/* testimonials */
.tcard{top:2931px;width:243px;height:245px;background:#fff;box-shadow:0 6px 24px rgba(0,0,0,.06);padding:28px 0 0 28px}
.quote{width:50px;height:48px;background:#fde3d3;color:#f3a77f;font-size:44px;font-weight:700;display:flex;align-items:center;justify-content:center;line-height:1;padding-top:16px}
.person{display:flex;gap:12px;align-items:center;margin-top:20px;margin-left:1px}
.avatar{width:46px;height:46px;border-radius:50%;background:#e7c9b4}
.person b{font-size:16px;font-weight:600;display:block;color:#1f2a4a}
.person small{font-size:12px;color:#666}
.tcard p{font-size:12px;line-height:1.7;color:#666;margin-top:10px;width:205px}

/* footer */
.flinks{left:437px;top:3684px;font-size:14px;line-height:27.6px}
.social{top:3907px;width:34px;height:34px;border-radius:50%;border:1px solid var(--line);display:flex;align-items:center;justify-content:center}
.social i{width:10px;height:10px;border-radius:50%;background:var(--ink);display:block}
</style>
</head>
<body>

<section class="abs hero">
  <div class="photo" role="img" aria-label="Bouquet of peach and white roses in a ceramic vase" style="left:560px;top:170px;width:640px;height:487px;background:radial-gradient(ellipse at 55% 40%,#f7cfc3 0%,#f2ddd6 45%,rgba(239,226,220,0) 75%)"></div>
</section>

<div class="abs brand"><span>Fern &amp; Folly</span><span class="dot"></span></div>
<nav class="abs nav"><span>Arrangements</span><span>Bouquets</span><span>Everlasting Arrangements</span><span>Gifts</span><span>Contact</span></nav>
<div class="abs tools">
  <svg width="18" height="18" viewBox="0 0 18 18" fill="none" stroke="#222" stroke-width="1.6"><circle cx="7.5" cy="7.5" r="6"/><path d="M12 12l5 5"/></svg>
  <svg width="18" height="18" viewBox="0 0 18 18" fill="none" stroke="#222" stroke-width="1.6"><circle cx="9" cy="6" r="4"/><path d="M2 17c1-4 4-6 7-6s6 2 7 6"/></svg>
  <svg width="19" height="18" viewBox="0 0 19 18" fill="none" stroke="#222" stroke-width="1.6"><path d="M9.5 16S2 11.5 2 6.5A3.8 3.8 0 0 1 9.5 5a3.8 3.8 0 0 1 7.5 1.5C17 11.5 9.5 16 9.5 16z"/></svg>
  <svg width="18" height="18" viewBox="0 0 18 18" fill="none" stroke="#222" stroke-width="1.6"><path d="M3 6h12l-1 11H4z"/><path d="M6 6V4a3 3 0 0 1 6 0v2"/></svg>
</div>
<div class="abs badge">2</div>
<div class="abs cart">Your Cart<b>$89.25</b></div>

<div class="abs script" style="left:120px;top:272px">Flower &amp; Gift</div>
<h1 class="abs heading" style="left:119px;top:302px;font-size:56px;font-weight:800">Get up to 75%</h1>
<p class="abs" style="left:120px;top:366px;width:430px;font-size:15px;line-height:1.65;color:var(--text)">Lorem Ipsum is simply dummy text of the printing and typesetting Lorem Ipsum has been industry's .</p>
<div class="abs btn" style="left:121px;top:428px;width:124px;height:30px">View All</div>
<div class="abs dots" style="left:578px;top:610px"><i class="on"></i><i></i><i></i></div>

<div class="abs cat" style="left:44px" role="img" aria-label="Mixed flower arrangement on pink"><div class="photo" style="inset:0;background:linear-gradient(135deg,#f4b5b7,#eaa0ad 60%,#cf7da8)"></div><div class="frame"></div><p>Flower<b>Arrangements</b></p></div>
<div class="abs cat" style="left:327px" role="img" aria-label="Red roses and lilies in a glass vase"><div class="photo" style="inset:0;background:linear-gradient(135deg,#ecdcda,#d98a92 55%,#b9485a)"></div><div class="frame"></div><p>Flower<b>Bouquets</b></p></div>
<div class="abs cat" style="left:608px" role="img" aria-label="Dried everlasting flower bunch held in hand"><div class="photo" style="inset:0;background:linear-gradient(135deg,#efece8,#e1d7c7 55%,#c6b195)"></div><div class="frame"></div><p>Everlasting<b>Arrangements</b></p></div>
<div class="abs cat" style="left:888px" role="img" aria-label="Wrapped gift box with pink blossoms"><div class="photo" style="inset:0;background:linear-gradient(135deg,#f4eeeb,#efdcd6 55%,#e7a6a2)"></div><div class="frame"></div><p>Flower<b>Gifts</b></p></div>

<div class="photo" role="img" aria-label="Pink daisies in a white pot" style="left:89px;top:1079px;width:241px;height:359px;background:linear-gradient(180deg,#f7d4db,#efb7cd 55%,#f4ebe9)"></div>
<div class="photo" role="img" aria-label="Pink and white tulips" style="left:336px;top:1036px;width:241px;height:219px;background:linear-gradient(135deg,#f8d7dd,#f3b9c4 55%,#e7a0b0)"></div>
<div class="photo" role="img" aria-label="Pink roses in a round kraft box" style="left:336px;top:1261px;width:241px;height:177px;background:linear-gradient(135deg,#f7e9ec,#e8a6c7 55%,#d6b07f)"></div>
<div class="abs script" style="left:663px;top:1150px">Fresh Flowers</div>
<h2 class="abs heading" style="left:663px;top:1189px;font-size:36px">From our garden<br>to your table</h2>
<p class="abs" style="left:663px;top:1275px;width:440px;font-size:15px;line-height:1.65;color:var(--text)">Flowers are carefully selected and handpicked by expert florists to bring smile and happiness.</p>
<div class="abs btn" style="left:660px;top:1335px;width:123px;height:31px">Buy Now</div>
<div class="photo" role="img" aria-label="Decorative yellow flower" style="left:964px;top:1435px;width:92px;height:92px;background:#fbf1d2"></div>

<div class="abs script center" style="top:1530px">Best Gifts</div>
<h2 class="abs heading center" style="top:1567px;font-size:37px">Our Product</h2>
<p class="abs center" style="top:1616px;font-size:15px;line-height:1.6;color:var(--text)">All varieties of flowers available in different shapes and types<br>special hand-tied bouquet</p>

<div class="abs prod" style="left:89px"><div class="img" role="img" aria-label="Red rose bouquet in kraft wrap" style="background:radial-gradient(ellipse at 50% 30%,#d6212c 0 35%,#e7c8a6 60%,rgba(255,255,255,0) 72%)"></div>
  <div class="info"><div class="stars">★★★★★</div><h4>Birthday Bouquet</h4><div class="price">$65.00</div><div class="sw"><i><span style="background:#e86a8c"></span></i><i><span style="background:#e6b1b8"></span></i><i><span style="background:#8e2f34"></span></i></div></div></div>
<div class="abs prod" style="left:345px"><div class="img" role="img" aria-label="White lilies and red tulips in a vase" style="background:radial-gradient(ellipse at 50% 35%,#f2eee8 0 25%,#c94f68 40%,#8eb07a 55%,rgba(255,255,255,0) 72%)"></div>
  <div class="info"><div class="stars">★★★★★</div><h4>Rose of Sharon</h4><div class="price">$65.00</div><div class="sw"><i><span style="background:#6e8f4e"></span></i><i><span style="background:#8b2135"></span></i><i><span style="background:#d6456d"></span></i></div></div></div>
<div class="abs prod" style="left:608px"><div class="img" role="img" aria-label="Cream and blush rose posy with ribbon" style="background:radial-gradient(ellipse at 50% 30%,#f1e4dc 0 30%,#c9b3a6 50%,rgba(255,255,255,0) 70%)"></div>
  <div class="info"><div class="stars">★★★★★</div><h4>Tea Rose</h4><div class="price">$65.00</div><div class="sw"><i><span style="background:#9c3a3a"></span></i><i><span style="background:#e07b2e"></span></i><i><span style="background:#7ea04a"></span></i></div></div></div>
<div class="abs prod" style="left:864px"><div class="img" role="img" aria-label="Pastel pink rose bouquet with eucalyptus" style="background:radial-gradient(ellipse at 50% 30%,#f2c6cc 0 30%,#a7bba0 52%,rgba(255,255,255,0) 70%)"></div>
  <div class="info"><div class="stars">★★★★★</div><h4>Tea Rose</h4><div class="price">$65.00</div><div class="sw"><i><span style="background:#b98bb3"></span></i><i><span style="background:#c2435a"></span></i><i><span style="background:#6d3a6e"></span></i></div></div></div>

<div class="abs script center" style="top:2132px">Order Now</div>
<h2 class="abs heading center" style="top:2170px;font-size:37px">Our Garden Collections</h2>
<p class="abs center" style="top:2219px;font-size:15px;line-height:1.6;color:var(--text)">Blossoms live in every color and aroma. Beautifully share your<br>emotions with our garden flowers.</p>

<div class="abs steps"></div>
<div class="photo" role="img" aria-label="Florist arranging a colourful bouquet in a flower studio" style="left:594px;top:2299px;width:515px;height:399px;background:linear-gradient(120deg,#ece7e4,#e3dcd9 40%,#e6a4b6 70%,#f1c94a)"></div>

<div class="abs step" style="top:2389px"><div class="icon"><svg width="40" height="40" viewBox="0 0 40 40" fill="none" stroke="#333" stroke-width="1.4"><circle cx="20" cy="20" r="5"/><ellipse cx="20" cy="9" rx="4" ry="6"/><ellipse cx="20" cy="31" rx="4" ry="6"/><ellipse cx="9" cy="20" rx="6" ry="4"/><ellipse cx="31" cy="20" rx="6" ry="4"/></svg></div><div><h5>Choose Flower</h5><p>Facilisis sed odio morbi quis commodo odio.<br>Tristique et egestas quis ipsum.</p></div></div>
<div class="abs step" style="top:2492px"><div class="icon"><svg width="40" height="40" viewBox="0 0 40 40" fill="none" stroke="#333" stroke-width="1.4"><rect x="8" y="6" width="22" height="28" rx="2"/><path d="M13 13h12M13 19h12M13 25h7"/><path d="M28 22l5 5-6 6h-4v-4z"/></svg></div><div><h5>Place an Order</h5><p>Facilisis sed odio morbi quis commodo odio.<br>Tristique et egestas quis ipsum.</p></div></div>
<div class="abs step" style="top:2595px"><div class="icon"><svg width="40" height="40" viewBox="0 0 40 40" fill="none" stroke="#333" stroke-width="1.4"><path d="M8 22h14l-2 12H10z"/><path d="M15 22V12M15 14c-3-2-6-1-7 1M15 14c3-3 6-2 7 0"/><rect x="24" y="24" width="10" height="10"/><path d="M29 24v-6M26 18h6"/></svg></div><div><h5>Get Plants Delivered</h5><p>Facilisis sed odio morbi quis commodo odio.<br>Tristique et egestas quis ipsum.</p></div></div>

<div class="abs script center" style="top:2820px">Testimonial</div>
<h2 class="abs heading center" style="top:2859px;font-size:37px">What Clients Says</h2>

<div class="abs tcard" style="left:222px"><div class="quote">“</div><div class="person"><div class="avatar" role="img" aria-label="Client portrait"></div><div><b>John smith</b><small>Co Founder</small></div></div><p>Lorem Ipsum is simply dummy text of the printing and typeset-ting industry .</p></div>
<div class="abs tcard" style="left:477px"><div class="quote">“</div><div class="person"><div class="avatar" role="img" aria-label="Client portrait" style="background:#d9b6a4"></div><div><b>John smith</b><small>Co Founder</small></div></div><p>Lorem Ipsum is simply dummy text of the printing and typeset-ting industry .</p></div>
<div class="abs tcard" style="left:738px"><div class="quote">“</div><div class="person"><div class="avatar" role="img" aria-label="Client portrait" style="background:#f2c94c"></div><div><b>John smith</b><small>Co Founder</small></div></div><p>Lorem Ipsum is simply dummy text of the printing and typeset-ting industry .</p></div>
<div class="abs dots" style="left:581px;top:3203px"><i class="on" style="background:var(--gold)"></i><i></i><i></i></div>

<div class="photo" role="img" aria-label="Florist smiling among bouquets" style="left:0;top:3284px;width:300px;height:291px;background:linear-gradient(135deg,#d8d1c7,#a9a695 50%,#e7d66e)"></div>
<div class="photo" role="img" aria-label="Hands arranging yellow roses" style="left:300px;top:3284px;width:300px;height:291px;background:linear-gradient(135deg,#b8a89a,#f0cf4a 55%,#e6a22c)"></div>
<div class="photo" role="img" aria-label="Flowers in a kraft shopping bag" style="left:600px;top:3284px;width:300px;height:291px;background:linear-gradient(135deg,#a8cbd6,#eeb8c3 50%,#d6a675)"></div>
<div class="photo" role="img" aria-label="Wooden crate of red and white flowers" style="left:900px;top:3284px;width:300px;height:291px;background:linear-gradient(135deg,#2b5ea9,#8c9aa6 50%,#c23a48)"></div>
<div class="abs" style="left:445px;top:3407px;width:310px;height:61px;background:#fbe4d3;display:flex;align-items:center;justify-content:center;font-size:36px;font-weight:700;letter-spacing:1px">#INSTAGRAM</div>

<div class="abs" style="left:92px;top:3735px;display:flex;align-items:center;gap:10px;font-size:30px;font-weight:400">Fern &amp; Folly<span style="width:12px;height:12px;border-radius:50%;background:var(--accent)"></span></div>
<ul class="abs flinks" style="list-style:none"><li>Arrangements</li><li>bouquets</li><li>everlasting arrangements</li><li>gifts</li><li>contact</li></ul>
<div class="abs" style="left:713px;top:3727px;width:389px;height:48px;border-bottom:1px solid var(--line);display:flex;align-items:center;font-size:16px">
  <svg width="22" height="12" viewBox="0 0 22 12" fill="none" stroke="#222" stroke-width="2" style="margin:0 12px"><path d="M0 6h19M14 1l5 5-5 5"/></svg>
  <span style="color:#888;flex:1">email address</span><span style="margin-right:14px;letter-spacing:.5px">SUBMIT</span></div>
<div class="abs" style="left:89px;top:3893px;width:1020px;height:1px;background:var(--line)"></div>
<p class="abs" style="left:89px;top:3914px;font-size:13px">©Copyright 2021 | All Rights Reserved</p>
<div class="abs social" style="left:993px"><i></i></div>
<div class="abs social" style="left:1036px"><i></i></div>
<div class="abs social" style="left:1077px"><i></i></div>

</body>
</html>
```